RTV CRAFTED

building services
decks
pergola
renovation
extensions
general building

Target Market(s)

middle to upper class

Industry/Entity Type

building

Contact Information for Business Card

my details 0427839152 pkharlow47@mailvane.net BLD574926

Font styles to use
Serif

Colors
00AB8E
00BBA5
67D7C9
C6EFE9
E9F9F6

Requirements
Must have
• logo on the front and details on the back
Nice to have
• sharp and clean lines

```html
<!DOCTYPE html>
<html lang="en">
<head>
<meta charset="utf-8">
<title>RTV CRAFTED business card</title>
<link rel="stylesheet" href="https://fonts.googleapis.com/css2?family=Karla:wght@400;500;700&display=swap">
<style>
  :root {
    --canvas: #9a9a9a;
    --paper: #ffffff;
    --charcoal: #353435;
    --ink: #111111;
    --muted: #555555;
    --green: #00b36d;
    --white: #ffffff;
  }
  * { box-sizing: border-box; margin: 0; padding: 0; }
  html, body { width: 1133px; height: 1200px; overflow: hidden; }
  body { background: var(--canvas); position: relative; font-family: "Karla", sans-serif; }

  .card { position: absolute; overflow: hidden; }
  .card--front { left: 192px; top: 139px; width: 734px; height: 417px; background: var(--paper); }
  .card--back { left: 196px; top: 641px; width: 728px; height: 416px; background: var(--charcoal); }

  .wordmark { font-family: "Karla", sans-serif; font-weight: 700; white-space: nowrap; letter-spacing: 3px; line-height: 1; }
  .card--front .wordmark { position: absolute; left: 0; right: 0; top: 112px; text-align: center; font-size: 42px; color: var(--ink); }

  .identity { position: absolute; right: 386px; top: 246px; text-align: right; }
  .identity__name { font-weight: 700; font-size: 23px; letter-spacing: 1px; color: var(--ink); line-height: 24px; }
  .identity__role { font-size: 16px; color: var(--green); letter-spacing: 0.5px; line-height: 22px; }

  .divider { position: absolute; left: 362px; top: 245px; width: 2px; height: 48px; background: var(--ink); }

  .contact { position: absolute; left: 378px; top: 246px; list-style: none; font-size: 16px; color: var(--muted); letter-spacing: 0.4px; }
  .contact li { display: flex; align-items: center; gap: 8px; height: 21px; }
  .contact svg { width: 13px; height: 13px; flex: none; }

  .licence { position: absolute; left: 0; right: 0; top: 338px; text-align: center; font-size: 16px; color: var(--muted); letter-spacing: 1px; }

  .edge-band { position: absolute; left: 0; bottom: 0; width: 734px; height: 17px; }

  .card--back .wordmark { position: absolute; left: 143px; top: 190px; font-size: 30px; color: var(--white); }

  .services { position: absolute; left: 436px; top: 149px; list-style: none; color: var(--white); font-size: 16px; letter-spacing: 0.5px; }
  .services li { display: flex; align-items: center; gap: 8px; height: 19.6px; }
  .services svg { width: 12px; height: 12px; flex: none; fill: none; stroke: var(--white); stroke-width: 1.8; }
</style>
</head>
<body>

<section class="card card--front">
  <div class="wordmark">RTV CRAFTED</div>

  <div class="identity">
    <p class="identity__name">DANIEL REEVES</p>
    <p class="identity__role">President</p>
  </div>
  <div class="divider"></div>

  <ul class="contact">
    <li>
      <svg viewBox="0 0 24 24"><path fill="var(--green)" d="M6.6 10.8c1.4 2.8 3.8 5.1 6.6 6.6l2.2-2.2c.3-.3.7-.4 1-.2 1.1.4 2.3.6 3.6.6.6 0 1 .4 1 1V20c0 .6-.4 1-1 1C10.6 21 3 13.4 3 4c0-.6.4-1 1-1h3.5c.6 0 1 .4 1 1 0 1.3.2 2.5.6 3.6.1.3 0 .7-.2 1z"/></svg>
      <span>042-783-9152</span>
    </li>
    <li>
      <svg viewBox="0 0 24 24"><rect x="2" y="5" width="20" height="14" fill="var(--green)"/><path d="M3 6l9 7 9-7" fill="none" stroke="var(--white)" stroke-width="2"/></svg>
      <span>pkharlow47@mailvane.net</span>
    </li>
  </ul>

  <p class="licence">BLD574926</p>

  <svg class="edge-band" viewBox="0 0 734 17" preserveAspectRatio="none">
    <polygon points="0,0 374,0 369,17 0,17" fill="var(--green)"/>
    <polygon points="379,0 734,0 734,17 374,17" fill="var(--ink)"/>
  </svg>
</section>

<section class="card card--back">
  <div class="wordmark">RTV CRAFTED</div>

  <ul class="services">
    <li><svg viewBox="0 0 12 12"><rect x="1" y="1" width="10" height="10"/><path d="M3 6l2 2 5-6"/></svg>Building Services</li>
    <li><svg viewBox="0 0 12 12"><rect x="1" y="1" width="10" height="10"/><path d="M3 6l2 2 5-6"/></svg>Decks</li>
    <li><svg viewBox="0 0 12 12"><rect x="1" y="1" width="10" height="10"/><path d="M3 6l2 2 5-6"/></svg>Pergola</li>
    <li><svg viewBox="0 0 12 12"><rect x="1" y="1" width="10" height="10"/><path d="M3 6l2 2 5-6"/></svg>Renovation</li>
    <li><svg viewBox="0 0 12 12"><rect x="1" y="1" width="10" height="10"/><path d="M3 6l2 2 5-6"/></svg>Extensions</li>
    <li><svg viewBox="0 0 12 12"><rect x="1" y="1" width="10" height="10"/><path d="M3 6l2 2 5-6"/></svg>General Building</li>
  </ul>
</section>

</body>
</html>
```